Vorlage für ein Workbook
Zielgruppe
Coaching und Beratung
Aufgabenstellung
Es soll eine Vorlage für ein Workbook erstellt werden, das ich dann selbst mit Inhalten füllen kann.. evtl. mit Canvas oder wie auch immer....
Es ist ein 12 Wochenkurs, d.h. ich brauche 1 Titelseite für jede Woche, die ich dann paste und copy machen kann und beschriften kann, sowie eine Vorlage für die einzelnen Seiten des Workbooks. Das Workbook in pdf Format muss auch online ausgefüllt werden können.
Design angepasst an Landingpage

```html
<!DOCTYPE html>
<html lang="de">
<head>
<meta charset="utf-8">
<title>Workbook Titelseiten – Vorlagen</title>
<link rel="stylesheet" href="https://fonts.googleapis.com/css2?family=Cinzel:wght@400&display=swap">
<style>
  :root{
    --board-top:#5f6a8b;
    --board-bottom:#aeb3c9;
    --paper:#ffffff;
    --sage:#b4bda6;
    --taupe:#c4bdb6;
    --line-warm:#c5bdb5;
    --line-light:#f6ecea;
    --ink:#4a4848;
    --title-sage:#b4bda6;
    --title-light:#ffffff;
  }
  *{margin:0;padding:0;box-sizing:border-box}
  html,body{width:848px;height:1200px;overflow:hidden}
  body{
    background:linear-gradient(200deg,var(--board-top) 0%,var(--board-bottom) 100%);
    font-family:"Cinzel",serif;
    position:relative;
  }
  .page{
    position:absolute;
    width:397px;height:563px;
    background:var(--paper);
    overflow:hidden;
  }
  .page--one{left:16px;top:27px}
  .page--two{left:436px;top:27px}
  .page--three{left:16px;top:610px}
  .page--four{left:436px;top:610px}
  .page__art{position:absolute;inset:0;width:100%;height:100%}
  .page__text{
    position:absolute;left:68px;top:201px;width:280px;
  }
  .page__title{
    font-family:"Cinzel",serif;
    font-weight:400;
    font-size:32px;
    line-height:1;
    color:var(--title-sage);
    letter-spacing:0;
    white-space:nowrap;
  }
  .page--four .page__title{color:var(--title-light)}
  .page__intro{
    margin-top:14px;
    font-size:7.6px;
    line-height:9.8px;
    color:var(--ink);
  }
</style>
</head>
<body>

<section class="page page--one">
  <svg class="page__art" viewBox="0 0 595 843" preserveAspectRatio="none">
    <path fill="var(--sage)" d="M384,0 H595 V202 C560,206 522,192 506,152 C490,110 505,55 384,0 Z"/>
    <path fill="var(--sage)" d="M0,355 C70,380 92,450 80,540 C68,640 120,690 230,700 C320,710 372,770 396,843 H0 Z"/>
    <path fill="none" stroke="var(--paper)" stroke-width="2" d="M0,405 C38,430 50,480 42,560 C34,650 80,695 190,705 C300,715 360,770 380,843"/>
    <path fill="none" stroke="var(--paper)" stroke-width="2" d="M0,450 C28,480 28,560 22,640 C18,720 90,755 190,757 C280,760 330,790 350,843"/>
    <rect role="img" aria-label="Zartes Zweig- und Beerenornament in Salbeigrün" x="0" y="0" width="225" height="262" fill="var(--sage)" opacity="0.28"/>
    <rect role="img" aria-label="Zweigornament mit Beeren in hellem Rosé auf Salbeigrün" x="505" y="28" width="90" height="172" fill="var(--line-light)" opacity="0.35"/>
  </svg>
  <div class="page__text">
    <h1 class="page__title">Lorem Ipsum</h1>
    <p class="page__intro">Lorem ipsum dolor sit amet, consectetuer adipiscing elit,<br>sed diam nonummy nibh euismod tincidunt ut laoreet<br>dolore magna aliquam</p>
  </div>
</section>

<section class="page page--two">
  <svg class="page__art" viewBox="0 0 595 843" preserveAspectRatio="none">
    <path fill="var(--taupe)" d="M5,5 H595 C590,80 520,132 400,140 C250,150 120,142 70,210 C42,250 20,280 5,295 Z"/>
    <path fill="none" stroke="var(--line-light)" stroke-width="1.2" d="M5,50 C80,30 170,40 200,90 C230,140 300,130 340,70 C380,10 470,0 560,5"/>
    <path fill="none" stroke="var(--line-light)" stroke-width="1.2" d="M5,95 C120,80 180,100 220,140 C260,185 320,185 360,130 C400,70 470,20 560,5"/>
    <path fill="none" stroke="var(--line-warm)" stroke-width="1.2" d="M595,388 C545,460 420,440 362,480 C330,510 342,600 347,680 C352,765 300,822 225,843"/>
    <path fill="none" stroke="var(--line-warm)" stroke-width="2" d="M595,548 C560,568 500,552 440,560 C400,568 396,620 396,690 V843"/>
    <path fill="none" stroke="var(--line-warm)" stroke-width="1.2" d="M595,598 C560,612 500,600 442,592 C420,590 418,640 428,700 L470,843"/>
    <rect role="img" aria-label="Linienzeichnung eines Blätterzweigs in Taupe" x="0" y="528" width="250" height="300" fill="var(--taupe)" opacity="0.25"/>
  </svg>
  <div class="page__text">
    <h1 class="page__title">Lorem Ipsum</h1>
    <p class="page__intro">Lorem ipsum dolor sit amet, consectetuer adipiscing elit,<br>sed diam nonummy nibh euismod tincidunt ut laoreet<br>dolore magna aliquam</p>
  </div>
</section>

<section class="page page--three">
  <svg class="page__art" viewBox="0 0 595 843" preserveAspectRatio="none">
    <path fill="var(--sage)" d="M415,0 H595 V75 C575,80 565,130 545,135 C522,140 515,102 482,106 C445,112 402,132 399,100 C396,62 402,22 415,0 Z"/>
    <path fill="none" stroke="var(--line-warm)" stroke-width="1.5" d="M348,0 C355,60 350,125 380,165 C410,190 470,150 505,140 C535,130 530,190 560,195 C580,198 590,180 595,175"/>
    <path fill="none" stroke="var(--line-warm)" stroke-width="1.2" d="M392,0 C380,60 365,150 398,170 C440,190 470,180 495,196 C520,215 550,250 595,265"/>
    <path fill="var(--sage)" d="M0,390 C50,388 80,420 78,470 C76,540 112,578 200,580 C292,582 300,650 352,682 C384,705 386,780 380,843 H0 Z"/>
    <path fill="none" stroke="var(--line-light)" stroke-width="2" d="M0,455 C40,482 50,530 52,600 C55,680 100,722 180,722 C262,722 332,742 420,843"/>
    <rect role="img" aria-label="Linienzeichnung eines Blätterzweigs in Salbeigrün" x="0" y="72" width="225" height="130" fill="var(--sage)" opacity="0.25"/>
  </svg>
  <div class="page__text">
    <h1 class="page__title">Lorem Ipsum</h1>
    <p class="page__intro">Lorem ipsum dolor sit amet, consectetuer adipiscing elit,<br>sed diam nonummy nibh euismod tincidunt ut laoreet<br>dolore magna aliquam</p>
  </div>
</section>

<section class="page page--four">
  <svg class="page__art" viewBox="0 0 595 843" preserveAspectRatio="none">
    <path fill="var(--taupe)" d="M190,0 C222,80 262,150 372,170 C472,190 520,212 520,300 C520,392 540,480 595,520 V843 H292 C200,843 160,780 150,720 C138,620 100,570 0,570 V0 Z"/>
    <path fill="none" stroke="var(--line-warm)" stroke-width="2" d="M212,0 C240,78 282,138 400,150 C500,160 542,200 552,300 C560,420 570,480 595,505"/>
    <rect role="img" aria-label="Zweigornament mit Beeren in hellem Rosé" x="0" y="0" width="180" height="210" fill="var(--line-light)" opacity="0.3"/>
    <rect role="img" aria-label="Großes Zweigornament mit Beeren in hellem Rosé" x="280" y="490" width="315" height="353" fill="var(--line-light)" opacity="0.3"/>
  </svg>
  <div class="page__text">
    <h1 class="page__title">Lorem Ipsum</h1>
    <p class="page__intro">Lorem ipsum dolor sit amet, consectetuer adipiscing elit,<br>sed diam nonummy nibh euismod tincidunt ut laoreet<br>dolore magna aliquam</p>
  </div>
</section>

</body>
</html>
```